its a new company based in Christchurch new Zealand building computers ,repairs, upgrades and anything computers for the general public,i like bright happy colours like yellows, greens reds anything that stands out and it needs to communicant trust and security towards my new company,i have no logo yet,

Target Market(s)

target market of all ages

Industry/Entity Type

Building

Contact Information for Business Card

Pixel Harbour Limited,ph-0274829315,email-brightnode47@mailvista.example,14c tamworth cl,kelvale

```html
<!DOCTYPE html>
<html lang="en">
<head>
<meta charset="utf-8">
<title>Pixel Harbour Limited – Business Card</title>
<link href="https://fonts.googleapis.com/css2?family=Quicksand:wght@500&family=Roboto:wght@300&display=swap" rel="stylesheet">
<style>
  :root {
    --brand-pink: #e8195f;
    --ink-navy: #1b2a3b;
    --icon-green: #8fe000;
    --green-deep: #4fbf00;
    --green-mid: #7fdc00;
    --green-bright: #b4ff1f;
    --ghost-grey: #eceef1;
    --paper: #ffffff;
  }
  * { margin: 0; padding: 0; box-sizing: border-box; }
  html, body { width: 1200px; height: 741px; overflow: hidden; background: var(--paper); }
  .card {
    position: relative;
    width: 1200px;
    height: 741px;
    background: var(--paper);
    overflow: hidden;
  }
  .swoosh { position: absolute; inset: 0; }
  .ghost-name {
    position: absolute;
    left: 930px;
    top: 250px;
    font-family: "Quicksand", sans-serif;
    font-weight: 500;
    font-size: 64px;
    line-height: 1.05;
    color: var(--ghost-grey);
  }
  .brand-mark {
    position: absolute;
    left: 52px;
    top: 150px;
    display: flex;
    align-items: center;
    gap: 16px;
  }
  .brand-mark__square {
    width: 34px;
    height: 34px;
    background: var(--ink-navy);
  }
  .brand-mark__name {
    font-family: "Quicksand", sans-serif;
    font-weight: 500;
    font-size: 38px;
    line-height: 1.1;
    color: var(--ink-navy);
  }
  .company-name {
    position: absolute;
    left: 274px;
    top: 62px;
    font-family: "Quicksand", sans-serif;
    font-weight: 500;
    font-size: 80px;
    letter-spacing: 1px;
    color: var(--brand-pink);
    white-space: nowrap;
  }
  .contact-list { list-style: none; }
  .contact-item {
    position: absolute;
    left: 300px;
    display: flex;
    align-items: center;
    gap: 30px;
    font-family: "Roboto", sans-serif;
    font-weight: 300;
    font-size: 44px;
    color: var(--ink-navy);
    white-space: nowrap;
  }
  .contact-item svg { flex: none; width: 62px; height: 62px; fill: var(--icon-green); }
  .contact-item--phone { top: 234px; }
  .contact-item--email { top: 336px; }
  .contact-item--address { top: 434px; }
</style>
</head>
<body>
<div class="card">
  <svg class="swoosh" width="1200" height="741" viewBox="0 0 1200 741" aria-hidden="true">
    <defs>
      <linearGradient id="green-sweep" x1="0" y1="0" x2="1" y2="0.3">
        <stop offset="0" stop-color="var(--green-deep)"/>
        <stop offset="0.55" stop-color="var(--green-mid)"/>
        <stop offset="1" stop-color="var(--green-bright)"/>
      </linearGradient>
    </defs>
    <path d="M0 395 C 180 520, 420 610, 640 600 C 860 590, 1040 530, 1200 488 L1200 741 L0 741 Z" fill="url(#green-sweep)"/>
    <path d="M0 470 C 200 600, 460 680, 720 660 C 930 645, 1080 600, 1200 570 L1200 741 L0 741 Z" fill="#ffffff" opacity="0.10"/>
    <path d="M0 560 C 220 680, 500 730, 800 705 C 980 690, 1110 660, 1200 640 L1200 741 L0 741 Z" fill="#ffffff" opacity="0.10"/>
    <path d="M0 650 C 260 740, 560 760, 900 735 L1200 720 L1200 741 L0 741 Z" fill="#ffffff" opacity="0.08"/>
  </svg>

  <div class="ghost-name" aria-hidden="true">Pixel<br>Harbour</div>

  <div class="brand-mark">
    <span class="brand-mark__square"></span>
    <span class="brand-mark__name">Pixel<br>Harbour</span>
  </div>

  <h1 class="company-name">Pixel Harbour Limited</h1>

  <ul class="contact-list">
    <li class="contact-item contact-item--phone">
      <svg viewBox="0 0 64 64" aria-hidden="true">
        <path d="M6 22 C6 12 20 8 32 8 C44 8 58 12 58 22 L58 26 L44 26 L44 20 C40 18 24 18 20 20 L20 26 L6 26 Z"/>
        <path d="M16 30 L24 26 L40 26 L48 30 L54 54 L10 54 Z"/>
        <circle cx="32" cy="40" r="7" fill="#ffffff"/>
        <circle cx="32" cy="40" r="3"/>
      </svg>
      <span>0274829315</span>
    </li>
    <li class="contact-item contact-item--email">
      <svg viewBox="0 0 64 64" aria-hidden="true">
        <path d="M4 14 L60 14 L60 50 L4 50 Z"/>
        <path d="M6 16 L32 36 L58 16" fill="none" stroke="#ffffff" stroke-width="3"/>
        <path d="M6 48 L24 30 M58 48 L40 30" fill="none" stroke="#ffffff" stroke-width="3"/>
      </svg>
      <span>brightnode47@mailvista.example</span>
    </li>
    <li class="contact-item contact-item--address">
      <svg viewBox="0 0 64 64" aria-hidden="true">
        <path d="M32 2 C19 2 10 11 10 23 C10 38 32 62 32 62 C32 62 54 38 54 23 C54 11 45 2 32 2 Z"/>
        <circle cx="32" cy="23" r="8" fill="#ffffff"/>
      </svg>
      <span>14c Tamworth Cl,Kelvale</span>
    </li>
  </ul>
</div>
</body>
</html>
```